Child Sponsorship Charity Needs a Wordpress Design

KinderHope GLOBALWORKS is a not-for-profit organization that breaks the cycle of poverty through child sponsorship. We work in 7 countries around the world and are based in Canada. We currently have a Wordpress website and want to update the look and create a more engaging user experience. Our donor base is across Canada and our partners work across the globe. PLEASE SEE THE DESIGN BRIEF ATTACHED. We are looking for out site to be clean, colourful, and inviting. It should maintain our brand image, be welcoming to potential donors, and a great resource to current donors.
Updates

Project Deadline Extended Reason: Our Board of Directors wants a chance to provide feedback on the submissions and so we are extending the deadline to give them the opportunity to share their insights. Added Saturday, February 21, 2015

Industry/Entity Type

Charity

Font styles to use
Other font styles liked:
• Helvetica / Helvetica Neue

Requirements
Must have
• Got a list of colours from the designer who made our logo:
• Kinderhope Navy blue
• C: 100
• M: 80
• Y: 0
• K: 23
• Or
• R: 2
• G: 60
• B: 132
• Kinderhope lighter blue
• C: 34
• M: 0
• Y: 3
• K: 0
• Or
• R: 161
• G: 221
• B: 241
• Kinderhope deep red (newsletter accent colour)
• C: 0
• M: 91
• Y: 88
• K: 30
• Or
• R: 178
• G: 44
• B: 34

```html
<!DOCTYPE html>
<html lang="en">
<head>
<meta charset="utf-8">
<title>KinderHope GLOBALWORKS</title>
<link rel="stylesheet" href="https://fonts.googleapis.com/css2?family=Open+Sans:wght@300;400;600&family=Quicksand:wght@600;700&display=swap">
<style>
:root{
  --top-blue:#2a5fae;
  --navy:#023c84;
  --news-blue:#0c3fa3;
  --orange:#ff8a00;
  --crimson:#b0003a;
  --pink:#f7909d;
  --brush-red:#c8002a;
  --brush-blue:#1443b0;
  --brush-orange:#f08a0a;
  --brush-magenta:#d80a62;
  --brush-wine:#b50a3c;
  --violet:#8f66d6;
  --white:#fff;
  --ink:#222;
  --grey:#777;
}
*{box-sizing:border-box;margin:0;padding:0}
html,body{width:893px;height:1200px;overflow:hidden}
body{position:relative;background:var(--white);font-family:Arial,"Helvetica Neue",Helvetica,sans-serif;color:var(--ink)}
.topbar{position:absolute;top:0;left:0;width:893px;height:27px;background:var(--top-blue);color:var(--white);font-size:8.5px;display:flex;align-items:center;padding-left:52px;gap:16px}
.topbar .socials{position:absolute;right:40px;top:5px;display:flex;gap:4px}
.topbar .socials span{width:17px;height:17px;border:1px solid rgba(255,255,255,.85);border-radius:50%}
.header{position:absolute;top:27px;left:0;width:893px;height:66px;background:var(--white)}
.brand{position:absolute;left:50px;top:10px;width:137px;height:50px;display:flex;align-items:center;gap:5px;padding-left:4px}
.brand .dot{width:14px;height:14px;border-radius:50%;background:var(--navy)}
.brand .name{font-size:10px;color:var(--navy)}
.nav{position:absolute;right:48px;top:28px;display:flex;gap:8px;font-family:"Open Sans",sans-serif;font-size:8px;color:#444}
.nav .active{color:#e0352a;border-bottom:1px solid #e0352a;padding-bottom:5px}
.hero{position:absolute;top:93px;left:0;width:893px;height:246px;background:linear-gradient(100deg,#d9c0a0 0%,#caa47e 45%,#c8a27a 100%)}
.pillars{position:absolute;top:339px;left:0;width:893px;height:96px;background:var(--orange);display:flex;padding:0 34px}
.pillar{width:206px;text-align:center;color:var(--white)}
.pillar h2{font-family:"Open Sans",sans-serif;font-weight:300;font-size:25px;margin-top:5px}
.pillar p{font-size:9px;line-height:14.5px;font-weight:bold;margin-top:4px;padding:0 10px}
.newsletter{position:absolute;top:435px;left:0;width:893px;height:120px;background:var(--crimson)}
.newsletter h3{position:absolute;left:92px;top:28px;font-family:"Open Sans",sans-serif;font-weight:300;font-size:25px;color:var(--white)}
.newsletter .field{position:absolute;left:462px;top:31px;width:180px;height:27px;background:var(--white);border-radius:3px}
.newsletter .subscribe{position:absolute;left:462px;top:65px;width:74px;height:21px;background:#333;color:var(--white);font-family:"Open Sans",sans-serif;font-size:8.5px;border-radius:3px;display:flex;align-items:center;justify-content:center}
.newsletter .donate{position:absolute;left:668px;top:31px;width:154px;height:30px;background:var(--violet);color:var(--white);font-family:"Open Sans",sans-serif;font-weight:600;font-size:12px;border-radius:3px;display:flex;align-items:center;justify-content:center}
.tiles{position:absolute;top:555px;left:0;width:893px;height:380px}
.tiles svg.bg{position:absolute;top:0;left:0}
.tile{position:absolute;width:250px;text-align:center}
.tile .label{margin:0 auto;width:160px;height:68px;border-radius:28px 40px 30px 44px;display:flex;align-items:center;justify-content:center;font-family:Quicksand,sans-serif;font-weight:700;font-size:20px;color:var(--white)}
.tile p{font-size:9.5px;line-height:14.6px;margin-top:18px;color:#222}
.news{position:absolute;top:945px;left:0;width:893px;height:206px;background:var(--news-blue)}
.news svg.edge{position:absolute;top:-12px;left:0}
.news h3{position:absolute;left:200px;top:22px;font-family:"Open Sans",sans-serif;font-weight:300;font-size:24px;color:#14224a}
.item{position:absolute;top:60px;width:170px;display:flex;gap:13px;color:var(--white)}
.item .thumb{width:40px;height:40px;border-radius:50%;background:#7f8ca0;flex:none;margin-top:3px}
.item p{font-size:9.5px;line-height:14.6px}
.item b{display:block;font-size:8px;margin-top:2px}
.photo{position:absolute;top:33px;height:140px;background:linear-gradient(160deg,#6c7fa6,#3c4f8f 55%,#c2b8a4)}
.next{position:absolute;left:848px;top:57px;width:18px;height:36px;background:#3a3a44;border-radius:3px;display:flex;align-items:center;justify-content:center}
.footer{position:absolute;top:1151px;left:0;width:893px;height:49px;background:#f4f4f4;border-top:1px solid #ddd}
.footer p{position:absolute;left:50px;top:40px;font-size:7.5px;color:var(--grey);white-space:nowrap}
.totop{position:absolute;width:22px;height:22px;border-radius:50%;background:#d7d7d7}
</style>
</head>
<body>
<div class="topbar">
  <span>&#9679; 118 – 2290 Maple Row, Brookvale, BC V0X 1A2</span>
  <span>Toll Free: 1-800-555-0142</span>
  <span>hello@kinderhopeglobal.org</span>
  <span>call</span>
  <span>24 / 7</span>
  <span style="margin-left:8px">Donate</span>
  <span>Contactez Nous</span>
  <div class="socials"><span></span><span></span><span></span><span></span><span></span></div>
</div>

<header class="header">
  <div class="brand"><span class="dot"></span><span class="name">KinderHope GLOBALWORKS</span></div>
  <nav class="nav"><span class="active">HOME</span><span>ABOUT US</span><span>PROGRAMS</span><span>WHERE WE WORK</span><span>GET INVOLVED</span><span>CONTACT</span><span>BOLOG</span><span>DONATE</span></nav>
</header>

<div class="hero" role="img" aria-label="Photo of a young girl holding a red pencil, looking up against a sandy textured wall"></div>

<section class="pillars">
  <div class="pillar"><h2>HOPE</h2><p>a few simple things might change child's life, or their world.</p></div>
  <div class="pillar"><h2>RESTORE</h2><p>recreating life with love,faith,trust and confidence</p></div>
  <div class="pillar"><h2>EDUCATE</h2><p>effective skill training and compensatory education to strengthen life</p></div>
  <div class="pillar"><h2>EMPOWER</h2><p>creation of an environment where child can walk with society</p></div>
</section>

<section class="newsletter">
  <h3>get our newsletter in your inbox</h3>
  <div class="field"></div>
  <div class="subscribe">Subscribe Now</div>
  <div class="donate">DONATE TO SUPPORT</div>
</section>

<section class="tiles">
  <svg class="bg" width="893" height="380" viewBox="0 0 893 380">
    <path fill="#f7909d" d="M0 12 L60 6 L120 14 L230 8 L300 16 L420 10 L540 17 L650 9 L760 14 L893 4 L893 362 L820 368 L700 366 L600 372 L480 366 L360 372 L240 364 L130 370 L40 362 L0 366 Z"/>
  </svg>
  <div class="tile" style="left:48px;top:40px"><div class="label" style="background:var(--brush-red)">about us</div><p>KinderHope GLOBALWORKS is a Christian charitable organization. We are loyal to our mission of breaking the cycle of poverty one child at a time</p></div>
  <div class="tile" style="left:323px;top:40px"><div class="label" style="background:var(--brush-blue)">programmes</div><p>Sponsoring a child through KinderHope GLOBALWORKS enables us to help meet the social, medical and emotional needs of a child living in poverty,</p></div>
  <div class="tile" style="left:598px;top:40px"><div class="label" style="background:var(--brush-orange)">where we work</div><p>KinderHope GLOBALWORKS currently works in 7 developing countries in the world: Haiti, Kenya, Mexico, Philippines, Sri Lanka, Thailand and Uganda.</p></div>
  <div class="tile" style="left:48px;top:222px"><div class="label" style="background:var(--brush-wine)">sponsor a child</div><p>Your monthly support of $40 CAD for sponsorship provides the opportunity for your sponsored child to have an education, access to healthcare</p></div>
  <div class="tile" style="left:323px;top:215px"><div class="label" style="background:var(--brush-magenta)">get involved</div><p>Join us in our mission of breaking the cycle of poverty and providing hope one child at a time through sponsorship!</p></div>
  <div class="tile" style="left:598px;top:215px"><div class="label" style="background:var(--brush-wine)">donate</div><p>Welcome to our Online Giving!Click here Sponsor a Child today Or give a gift to one of the programs listed in the sidebar...</p></div>
</section>

<section class="news">
  <svg class="edge" width="893" height="14" viewBox="0 0 893 14"><path fill="#0c3fa3" d="M0 10 L90 6 L200 10 L320 4 L460 9 L600 3 L720 8 L893 2 L893 14 L0 14 Z"/></svg>
  <h3>Latest news &amp; Blogs</h3>
  <div class="item" style="left:27px"><span class="thumb"></span><p>House of Lords speaker praises the Minister's women empowerment agenda<b>February 18, 2015</b></p></div>
  <div class="item" style="left:223px"><span class="thumb" style="background:#5f8a55"></span><p>Lorem Ipsum is simply dummy text of the printing and typesetting industry<b>February 18, 2015</b></p></div>
  <div class="item" style="left:419px"><span class="thumb" style="background:#8a7566"></span><p>Senator Rhee talks about women empowerment, global warming at Lakeview Hall<b>February 18, 2015</b></p></div>
  <div class="photo" style="left:589px;width:89px" role="img" aria-label="Photo of a schoolchild in a blue uniform writing in a notebook"></div>
  <div class="photo" style="left:691px;width:155px" role="img" aria-label="Photo of a smiling student writing at a classroom desk"></div>
  <div class="photo" style="left:859px;width:11px" role="img" aria-label="Edge of the next photo in the slider"></div>
  <div class="next"><svg width="8" height="12" viewBox="0 0 8 12"><path d="M2 1 L7 6 L2 11" stroke="#fff" stroke-width="1.6" fill="none"/></svg></div>
</section>
<span class="totop" style="left:864px;top:936px"></span>

<footer class="footer">
  <p>Powered By : brightframe | Privacy policy | © kinderhope canada 2015, all rights reserved | Toll Free no 1800 55 01 | email - help@kinderhopeglobal.org</p>
  <span class="totop" style="left:864px;top:33px"></span>
</footer>
</body>
</html>
```